Letterhead Design for Law Firm that Specializes in Property Damage Litigation

We are looking for a redesign of our letterhead. Our current letterhead lists all of our current staff members and we'd like to come up with a design that does NOT list all of the staff members so that it does not need to be updated with every newly hired employee. Must be in editable format.

We are a law firm that specializes in property damage, so we need something that is professional, yet modern. The final design should use our existing logo and should use a blue color scheme (alternate colors would be gray, black, and white).

Industry/Entity Type

Legal

Colors
0054AA
0677BA
7BADD7
CADEEF
E8F1F8

```html
<!DOCTYPE html>
<html lang="en">
<head>
<meta charset="utf-8">
<title>Hartwell Rennick &amp; Osler Letterhead</title>
<link rel="stylesheet" href="https://fonts.googleapis.com/css2?family=Cinzel:wght@500&family=Rajdhani:wght@500;700&family=Barlow:wght@600&display=swap">
<style>
  :root {
    --navy: #0f2f5e;
    --navy-deep: #0b2a57;
    --olive: #6b6a58;
    --gray-text: #55575b;
    --backdrop: #c4c5c7;
    --paper: #ffffff;
    --photo-light: #a3adbd;
    --photo-dark: #5f6d84;
  }
  * { margin: 0; padding: 0; box-sizing: border-box; }
  html, body {
    width: 1200px; height: 1177px; overflow: hidden;
    background: var(--backdrop);
  }
  .letterhead {
    position: absolute; left: 175px; top: 38px;
    width: 850px; height: 1100px;
    background: var(--paper);
    box-shadow: 0 2px 10px rgba(0,0,0,0.18);
    overflow: hidden;
  }
  .brand { position: absolute; left: 51px; top: 58px; }
  .brand-square {
    position: absolute; left: 8px; top: 14px;
    width: 90px; height: 68px; background: #6d6e70;
  }
  .brand-name {
    position: absolute; left: 121px; top: 0;
    font-family: "Cinzel", serif; font-weight: 500;
    font-size: 29px; line-height: 32px; color: var(--navy);
    white-space: nowrap;
  }
  .tagline {
    position: absolute; left: 49px; top: 164px;
    font-family: "Barlow", sans-serif; font-weight: 600;
    font-size: 13px; letter-spacing: 2.6px; color: var(--gray-text);
    white-space: nowrap;
  }
  .header-art { position: absolute; left: 0; top: 0; }
  .footer-art { position: absolute; left: 0; top: 950px; }
  .contact-label {
    position: absolute; left: 45px; top: 958px;
    font-family: "Cinzel", serif; font-weight: 500;
    font-size: 18px; line-height: 22px; color: #fff; letter-spacing: 0.5px;
  }
  .office {
    position: absolute; top: 1000px;
    font-family: "Rajdhani", sans-serif; font-weight: 500;
    font-size: 15.5px; line-height: 16.7px; color: #fff;
    white-space: nowrap;
  }
  .office--pa { left: 27px; }
  .office--nj { left: 315px; }
  .office h3 {
    font-weight: 700; font-size: 15.5px; margin-left: 16px;
    letter-spacing: 0.2px;
  }
  .office .line { display: flex; align-items: center; }
  .office .line svg { width: 10px; height: 10px; margin-right: 6px; flex: none; }
  .office .line.indent { padding-left: 16px; }
</style>
</head>
<body>
<div class="letterhead">

  <svg class="header-art" width="850" height="190" viewBox="0 0 850 190">
    <defs>
      <linearGradient id="skyline-tone" x1="0" y1="0" x2="0" y2="1">
        <stop offset="0" stop-color="var(--photo-light)"/>
        <stop offset="0.55" stop-color="var(--photo-dark)"/>
        <stop offset="1" stop-color="#8390a3"/>
      </linearGradient>
    </defs>
    <polygon role="img" aria-label="Photo of a suspension bridge and city skyline reflected in a river"
             points="329,0 850,0 850,175 500,175" fill="url(#skyline-tone)"/>
    <rect x="548" y="179" width="302" height="8" fill="var(--navy)"/>
  </svg>

  <div class="brand">
    <div class="brand-square"></div>
    <div class="brand-name">Hartwell<br>Rennick &amp;<br>Osler</div>
  </div>
  <div class="tagline">THE PROPERTY DAMAGE ATTORNEYS</div>

  <svg class="footer-art" width="850" height="150" viewBox="0 0 850 150">
    <polygon points="0,6 168,6 185,35 12,35" fill="var(--olive)"/>
    <polygon points="0,35 566,35 670,150 0,150" fill="var(--navy-deep)"/>
    <polygon points="576,35 590,35 702,150 688,150" fill="var(--olive)"/>
  </svg>
  <div class="contact-label">CONTACT</div>

  <div class="office office--pa">
    <h3>PHILADELPHIA OFFICE</h3>
    <div class="line"><svg viewBox="0 0 10 10"><path d="M5 0a3.6 3.6 0 0 0-3.6 3.6C1.4 6.3 5 10 5 10s3.6-3.7 3.6-6.4A3.6 3.6 0 0 0 5 0zm0 5a1.4 1.4 0 1 1 0-2.8A1.4 1.4 0 0 1 5 5z" fill="#fff"/></svg>2240 Market Crest Blvd. Suite 1180</div>
    <div class="line indent">Philadelphia, PA 19104</div>
    <div class="line"><svg viewBox="0 0 10 10"><path d="M2 .5l1.6 2.2-1 1.1a6 6 0 0 0 3.6 3.6l1.1-1 2.2 1.6-.9 1.5C4.7 9.5.5 5.3.5 1.4z" fill="#fff"/></svg>Phone: (215) 555-0140</div>
    <div class="line"><svg viewBox="0 0 10 10"><path d="M2.5 0h5v3h-5zM1 3.5h8v4H7.5V10h-5V7.5H1zm2.5 3v2.5h3V6.5z" fill="#fff"/></svg>Fax: (215) 555-0187</div>
  </div>

  <div class="office office--nj">
    <h3>NEW JERSEY OFFICE</h3>
    <div class="line"><svg viewBox="0 0 10 10"><path d="M5 0a3.6 3.6 0 0 0-3.6 3.6C1.4 6.3 5 10 5 10s3.6-3.7 3.6-6.4A3.6 3.6 0 0 0 5 0zm0 5a1.4 1.4 0 1 1 0-2.8A1.4 1.4 0 0 1 5 5z" fill="#fff"/></svg>880 Linden Avenue East, Suite 310</div>
    <div class="line indent">Cherry Hill, NJ 08002</div>
    <div class="line"><svg viewBox="0 0 10 10"><path d="M2 .5l1.6 2.2-1 1.1a6 6 0 0 0 3.6 3.6l1.1-1 2.2 1.6-.9 1.5C4.7 9.5.5 5.3.5 1.4z" fill="#fff"/></svg>Phone: (856) 555-0162</div>
    <div class="line"><svg viewBox="0 0 10 10"><path d="M2.5 0h5v3h-5zM1 3.5h8v4H7.5V10h-5V7.5H1zm2.5 3v2.5h3V6.5z" fill="#fff"/></svg>Fax: (856) 555-0119</div>
  </div>

</div>
</body>
</html>
```